Hello my name is Colin, I am Starting a business called Harbor Health and fitness and am in need of a memorable business card.
It is a personal training studio. I have added the logo that i would like to be on the left center om my business card. i would like room left up the top for a heading sentence such as. "Is your body shocking for all the wrong reasons". there must be room left on the right of the logo below the main heading for 3 sub headings.
then under those 3 headings and logo room for another larger heading eg. "give me a call and learn how to eat chocolate, drink bear and have great sex". in what room is left i would like to be used for my contact details, use I'm Colin Fairweather your fitness expert on the left then on the right Phone, Email and website space in at least 12 Point. Very specific i know :) now onto the back, for the back i would like an eye catching graphic and room for one main headline and 3 bullet points centered just write anything i will choose what to put in them when i pick a winner. Thank you very much for sticking through all of that :) i appreciate you taking the time to read it and hopefully undergo designing me a business card.
I can't wait to see the designs!

Target Market(s)

slightly more towards females although it would probably be best if it was targeted towards both sexes

Industry/Entity Type

Training

Requirements
Nice to have
• I would love to see if anyone could come up with a design that would really make my card stand out and be memorable.
Should not have
• tacky fitness photos of abs and muscles etc.

```html
<!DOCTYPE html>
<html lang="en">
<head>
<meta charset="utf-8">
<title>Harbor Health and Fitness – Business Card</title>
<link rel="stylesheet" href="https://fonts.googleapis.com/css2?family=Jost:wght@400;500&family=Arimo:ital,wght@0,400;0,700;1,400&display=swap">
<style>
  :root {
    --sky: #0aa6e6;
    --sea: #2c6aa3;
    --navy: #2e3192;
    --deep: #0d4a80;
    --cyan: #1ba9e3;
    --white: #ffffff;
    --icon: #1f8fd0;
  }
  * { box-sizing: border-box; margin: 0; padding: 0; }
  html, body { width: 1036px; height: 1200px; overflow: hidden; }
  body {
    position: relative;
    background: linear-gradient(180deg, var(--sky) 0%, #1892d2 40%, var(--sea) 100%);
    font-family: "Arimo", Arial, sans-serif;
  }
  .side-label {
    position: absolute;
    left: 660px;
    color: var(--white);
    font: 400 26px "Arimo", Arial, sans-serif;
  }
  .side-label.front { top: 58px; }
  .side-label.back { top: 1124px; }

  .card {
    position: absolute;
    left: 104px;
    width: 814px;
    height: 465px;
    overflow: hidden;
    box-shadow: 0 22px 34px rgba(0, 30, 70, 0.35);
  }
  .card-front { top: 120px; background: var(--white); }
  .card-back {
    top: 634px;
    background: linear-gradient(125deg, var(--deep) 0%, var(--deep) 22%, #3d97d6 50%, var(--deep) 66%, var(--deep) 100%);
  }

  .brand { position: absolute; color: #1c4f8c; font-family: "Jost", sans-serif; font-weight: 400; line-height: 1; }
  .brand .brand-name { display: block; font-size: 92px; letter-spacing: -1px; }
  .brand .brand-tag { display: block; font-size: 24px; margin-top: 4px; padding-left: 84px; }
  .card-front .brand { left: 74px; top: 44px; }

  .headline {
    position: absolute;
    left: 466px;
    top: 52px;
    width: 340px;
    color: var(--navy);
    font: 500 46px/50px "Jost", sans-serif;
    letter-spacing: -2.2px;
  }
  .offer-box {
    position: absolute;
    left: 458px;
    top: 222px;
    width: 356px;
    height: 140px;
    border-radius: 6px 0 0 6px;
    background: linear-gradient(60deg, var(--cyan) 0%, #2a80c0 45%, var(--deep) 100%);
  }
  .offer-tab {
    position: absolute;
    left: -2px;
    top: 56px;
    width: 20px;
    height: 26px;
    border-radius: 0 13px 13px 0;
    background: var(--white);
  }
  .offer-text {
    position: absolute;
    left: 48px;
    top: 30px;
    color: var(--white);
    font: 400 18px/24px "Jost", sans-serif;
  }
  .person { position: absolute; left: 82px; top: 228px; color: var(--navy); }
  .person-name { font: 700 24px "Arimo", Arial, sans-serif; }
  .person-role { font: italic 400 21px "Arimo", Arial, sans-serif; margin-top: 3px; }
  .contacts { position: absolute; left: 82px; top: 332px; list-style: none; color: var(--navy); font-size: 19.5px; }
  .contacts li { display: flex; align-items: center; height: 27px; }
  .contacts svg { width: 18px; height: 18px; margin-right: 10px; }
  .website { position: absolute; left: 463px; top: 407px; color: var(--navy); font: 700 20px "Arimo", Arial, sans-serif; }

  .subheads { position: absolute; left: 116px; top: 70px; list-style: none; color: var(--white); font-size: 24px; }
  .subheads li { height: 49px; }
  .hero-art {
    position: absolute;
    left: 461px;
    top: 16px;
    width: 290px;
    height: 297px;
    background: linear-gradient(180deg, rgba(170, 200, 225, 0.55), rgba(170, 200, 225, 0.85));
    border-radius: 40px 40px 0 0;
  }
  .back-band {
    position: absolute;
    left: -2px;
    top: 313px;
    width: 816px;
    height: 109px;
    background: var(--white);
  }
  .back-band .brand { left: 113px; top: 10px; }
  .back-band .brand .brand-name { font-size: 70px; }
  .back-band .brand .brand-tag { font-size: 19px; padding-left: 64px; margin-top: 2px; }
  .band-arrow { position: absolute; left: 447px; top: 40px; width: 30px; height: 30px; }
  .band-text { position: absolute; left: 502px; top: 16px; color: var(--navy); font: 400 18px/24px "Jost", sans-serif; }
  .back-strip {
    position: absolute;
    left: 0;
    top: 422px;
    width: 814px;
    height: 43px;
    background: linear-gradient(90deg, var(--cyan) 0%, #2a8ccc 60%, #2f6fa8 100%);
  }
</style>
</head>
<body>
  <div class="side-label front">Bizcard Front</div>

  <section class="card card-front">
    <div class="brand">
      <span class="brand-name">Harbor</span>
      <span class="brand-tag">Health and Fitness</span>
    </div>

    <h1 class="headline">Is your body shocking for all the wrong reasons</h1>

    <div class="offer-box">
      <span class="offer-tab"></span>
      <svg style="position:absolute;left:2px;top:62px" width="12" height="14" viewBox="0 0 12 14"><path d="M3 2l6 5-6 5" fill="none" stroke="#2e3192" stroke-width="2"/></svg>
      <p class="offer-text">Give me a call and learn how<br>to eat chocolate, drink bear<br>and have great sex</p>
    </div>

    <div class="person">
      <div class="person-name">Colin Fairweather</div>
      <div class="person-role">FITNESS EXPERT</div>
    </div>

    <ul class="contacts">
      <li><svg viewBox="0 0 18 18"><circle cx="9" cy="9" r="8" fill="none" stroke="var(--icon)" stroke-width="1.5"/><path d="M6 5l2 2-1 1.2c.6 1.3 1.5 2.2 2.8 2.8L11 10l2 2-1.3 1.3C8.5 12.8 5.2 9.5 4.7 6.3z" fill="var(--icon)"/></svg>555-014-2236</li>
      <li><svg viewBox="0 0 18 18"><circle cx="9" cy="9" r="8" fill="none" stroke="var(--icon)" stroke-width="1.5"/><rect x="6.5" y="4" width="5" height="10" rx="1" fill="none" stroke="var(--icon)" stroke-width="1.4" transform="rotate(25 9 9)"/></svg>XXX-XXX-XXXX</li>
      <li><svg viewBox="0 0 18 18"><circle cx="9" cy="9" r="8" fill="none" stroke="var(--icon)" stroke-width="1.5"/><rect x="5" y="7" width="8" height="5" rx="1" fill="var(--icon)"/><rect x="6.5" y="4.5" width="5" height="3" fill="none" stroke="var(--icon)" stroke-width="1.2"/></svg>555-019-4470</li>
      <li><svg viewBox="0 0 18 18"><circle cx="9" cy="9" r="8" fill="none" stroke="var(--icon)" stroke-width="1.5"/><text x="9" y="13" text-anchor="middle" font-size="11" font-family="Arial, sans-serif" fill="var(--icon)">@</text></svg>colin@harborhealth.com</li>
    </ul>

    <div class="website">www.harborhealth.com</div>
  </section>

  <section class="card card-back">
    <ul class="subheads">
      <li>1 sub headings</li>
      <li>2 sub headings</li>
      <li>3 sub headings</li>
    </ul>

    <div class="hero-art" role="img" aria-label="Silhouette of a woman running on a treadmill"></div>

    <div class="back-band">
      <div class="brand">
        <span class="brand-name">Harbor</span>
        <span class="brand-tag">Health and Fitness</span>
      </div>
      <svg class="band-arrow" viewBox="0 0 30 30"><circle cx="15" cy="15" r="14" fill="var(--navy)"/><path d="M13 10l5 5-5 5" fill="none" stroke="#fff" stroke-width="2"/></svg>
      <p class="band-text">Give me a call and learn how<br>to eat chocolate, drink bear<br>and have great sex</p>
    </div>
    <div class="back-strip"></div>
  </section>

  <div class="side-label back">Bizcard Back</div>
</body>
</html>
```